Magazine Cover & Back, Course Overview

Please read this whole description and follow directions before proceeding. Please do not submit multiple designs that look similar. If you submit multiple designs that look similar you will be disqualified and receive a poor rating. A magazine design includes a cover and back. This is a single design and should be submitted as such. Do not submit one design for the front only, then a separate design for the back, then a third mock up. Submit all as a single design. I need a magazine cover and back. The size will be standard paper size, 8-1/2" x 11". It will be used for a course overview, a summary of a boating instruction course. I have attached examples and pictures that can be used. I have also attached required content. The final designs must NOT be AI files. Text must be editable with Adobe Acrobat DC.

Target Market(s)

Military & Government

Industry/Entity Type

Military & Government

Requirements
Must have
• See attached.
Nice to have
• See attached.
Should not have
• See attached.

```html
<!DOCTYPE html>
<html lang="en">
<head>
<meta charset="utf-8">
<title>Diver Support Vessel Training – Course Overview</title>
<link rel="stylesheet" href="https://fonts.googleapis.com/css2?family=Archivo+Black&family=Montserrat:wght@500;600&family=Roboto+Condensed:wght@700&display=swap">
<style>
  :root{
    --stage:#ffffff;
    --sky-top:#2f66d8;
    --sky-mid:#6f9ff0;
    --shore:#5a4e47;
    --water:#2a4f8e;
    --deep:#0f1c3a;
    --band:rgba(40,90,210,.78);
    --white:#ffffff;
    --lavender:#a9a6d6;
    --tick:#f1c40f;
    --back-paper:#f7f7f8;
    --back-photo:#c9cacd;
    --logo-ink:#2c3546;
  }
  *{box-sizing:border-box;margin:0;padding:0}
  html,body{width:1200px;height:2462px;overflow:hidden;background:var(--stage)}
  .spread{position:relative;width:1200px;height:2462px}
  .page{position:absolute;left:160px;width:880px;height:1139px;overflow:hidden;box-shadow:0 6px 18px rgba(0,0,0,.25)}
  .page--front{top:62px}
  .page--back{top:1263px;background:var(--back-paper)}

  .cover-photo{position:absolute;inset:0;
    background:linear-gradient(180deg,var(--sky-top) 0%,var(--sky-mid) 26%,#a9b9cf 31%,var(--shore) 34%,#3d5f9c 37%,var(--water) 60%,#1d3567 82%,var(--deep) 100%)}

  .brand{position:absolute;display:flex;align-items:center;font-family:"Montserrat",sans-serif;font-weight:600}
  .brand__name{line-height:1.1}
  .brand__name b{display:block;font-weight:600}
  .brand__rule{width:2px;align-self:stretch}
  .brand__seal{border-radius:50%}

  .page--front .brand{left:60px;top:40px;color:var(--white)}
  .page--front .brand__name b:first-child{font-size:36px}
  .page--front .brand__name b:last-child{font-size:16px;letter-spacing:2px;text-align:right}
  .page--front .brand__rule{background:rgba(255,255,255,.7);margin:0 20px}
  .page--front .brand__seal{width:64px;height:64px;background:#1a1a1a;border:4px solid var(--tick)}

  .topic-band{position:absolute;left:486px;top:111px;width:394px;height:160px;background:var(--band);
    font-family:"Roboto Condensed",sans-serif;font-weight:700;color:var(--white);text-align:center;padding-top:10px}
  .topic-band span{display:block;line-height:.95}
  .topic-band .topic-band__lead{font-size:98px}
  .topic-band .topic-band__sub{font-size:70px}

  .title{position:absolute;inset:0}

  .features{position:absolute;left:61px;top:930px;width:780px;display:grid;grid-template-columns:300px 1fr;column-gap:30px;row-gap:18px;
    font-family:"Montserrat",sans-serif;font-weight:500;font-size:15.5px;line-height:1.3;color:var(--white);list-style:none}
  .features li{display:flex;gap:12px}
  .features svg{flex:none;width:19px;height:19px;margin-top:1px}

  .page--back .brand{left:195px;top:190px;color:var(--logo-ink)}
  .page--back .brand__name b:first-child{font-size:44px}
  .page--back .brand__name b:last-child{font-size:19px;letter-spacing:2px;text-align:right}
  .page--back .brand__rule{background:#7d8694;margin:0 22px}
  .page--back .brand__seal{width:92px;height:92px;background:#1a1a1a;border:5px solid var(--tick)}
  .back-photo{position:absolute;left:0;right:0;top:600px;bottom:0;
    background:linear-gradient(180deg,var(--back-paper) 0%,#dcdddf 22%,var(--back-photo) 45%,#b9babd 100%)}
</style>
</head>
<body>
<main class="spread">

  <section class="page page--front" aria-label="Front cover">
    <div class="cover-photo" role="img" aria-label="Grey diver support vessel flying a US flag underway on a blue lake with wooded shoreline and clear sky"></div>

    <div class="brand">
      <div class="brand__name"><b>Harbor Line</b><b>Marine Services, LLC</b></div>
      <span class="brand__rule"></span>
      <span class="brand__seal"></span>
    </div>

    <div class="topic-band">
      <span class="topic-band__lead">DIVER</span>
      <span class="topic-band__sub">SUPPORT</span>
    </div>

    <svg class="title" viewBox="0 0 880 1139" aria-label="Vessel Training">
      <defs>
        <linearGradient id="titleFill" x1="0" y1="0" x2="0" y2="1">
          <stop offset="0" stop-color="#ffffff"/>
          <stop offset=".55" stop-color="#ffffff"/>
          <stop offset="1" stop-color="#a9a6d6"/>
        </linearGradient>
        <linearGradient id="vFill" x1="0" y1="0" x2="0" y2="1">
          <stop offset="0" stop-color="#ffffff"/>
          <stop offset=".7" stop-color="#ffffff" stop-opacity=".95"/>
          <stop offset="1" stop-color="#ffffff" stop-opacity=".35"/>
        </linearGradient>
      </defs>
      <text x="56" y="750" font-family="Archivo Black, sans-serif" font-size="650" textLength="400" lengthAdjust="spacingAndGlyphs" fill="url(#vFill)">V</text>
      <text x="340" y="750" font-family="Archivo Black, sans-serif" font-size="162" textLength="474" lengthAdjust="spacingAndGlyphs" fill="url(#titleFill)">ESSEL</text>
      <text x="61" y="896" font-family="Archivo Black, sans-serif" font-size="146" textLength="753" lengthAdjust="spacingAndGlyphs" fill="url(#titleFill)">TRAINING</text>
    </svg>

    <ul class="features">
      <li><svg viewBox="0 0 20 20"><rect x="1.5" y="3.5" width="14" height="14" fill="none" stroke="#f1c40f" stroke-width="2"/><path d="M5 10l4 4 9-11" fill="none" stroke="#f1c40f" stroke-width="2.4"/></svg><span>To assist Navy Sailors with Becoming More Proficient Coxswains</span></li>
      <li><svg viewBox="0 0 20 20"><rect x="1.5" y="3.5" width="14" height="14" fill="none" stroke="#f1c40f" stroke-width="2"/><path d="M5 10l4 4 9-11" fill="none" stroke="#f1c40f" stroke-width="2.4"/></svg><span>Custom Made Course for Specific Users, Scenarios and Vessels Based on OIC Involvement, Client Feedback and After Action Reviews</span></li>
      <li style="grid-row:span 2"><svg viewBox="0 0 20 20"><rect x="1.5" y="3.5" width="14" height="14" fill="none" stroke="#f1c40f" stroke-width="2"/><path d="M5 10l4 4 9-11" fill="none" stroke="#f1c40f" stroke-width="2.4"/></svg><span>Focused on Safety &amp;<br>Close-Quarters<br>Maneuvering</span></li>
      <li><svg viewBox="0 0 20 20"><rect x="1.5" y="3.5" width="14" height="14" fill="none" stroke="#f1c40f" stroke-width="2"/><path d="M5 10l4 4 9-11" fill="none" stroke="#f1c40f" stroke-width="2.4"/></svg><span>Taught by Reputable USCG Licensed Boat Captains</span></li>
      <li><svg viewBox="0 0 20 20"><rect x="1.5" y="3.5" width="14" height="14" fill="none" stroke="#f1c40f" stroke-width="2"/><path d="M5 10l4 4 9-11" fill="none" stroke="#f1c40f" stroke-width="2.4"/></svg><span>Includes Useful Aids</span></li>
    </ul>
  </section>

  <section class="page page--back" aria-label="Back cover">
    <div class="back-photo" role="img" aria-label="Faded greyscale photo of the diver support vessel on the water with a hilly shoreline"></div>
    <div class="brand">
      <div class="brand__name"><b>Harbor Line</b><b>Marine Services, LLC</b></div>
      <span class="brand__rule"></span>
      <span class="brand__seal"></span>
    </div>
  </section>

</main>
</body>
</html>
```